MRW Snack Box for Printed Packaging

This is a TVW style 2 piece snack box. We have a jpeg logo and need it to be applied to the box along with some form of creative design. I have uploaded the keyline for the package. Please lay out the logo and design on this. Please bear in mind that the carton will be folded and appear like the photo which is also uploaded

Target Market(s)

General consumers in St. Lucia in the caribbean

Colors
EB3D1F
EC4F4E
F09395
F8D3D4
FCEDEE

```html
<!DOCTYPE html>
<html lang="en">
<head>
<meta charset="utf-8">
<title>MRW Snack Box Keyline</title>
<link rel="stylesheet" href="https://fonts.googleapis.com/css2?family=Anton&family=Montserrat:wght@600;800&display=swap">
<style>
  :root{
    --brand-red:#EB1C1F;
    --brand-red-soft:#EC4F4E;
    --brand-pink:#F09395;
    --brand-blush:#F8D3D4;
    --board-white:#FFFFFF;
    --table-grey:#DCDCDC;
    --keyline:#C8C8C8;
  }
  html,body{margin:0;padding:0;overflow:hidden;background:var(--table-grey);}
  .canvas{display:block;width:1200px;height:432px;}
  .board{fill:var(--board-white);stroke:var(--keyline);stroke-width:.6;}
  .red{fill:var(--brand-red);}
  .red-soft{fill:var(--brand-red-soft);}
  .headline{font-family:"Anton",sans-serif;fill:var(--board-white);}
  .brand-name{font-family:"Anton",sans-serif;fill:var(--brand-red);}
  .label{font-family:"Montserrat",sans-serif;font-weight:600;}
  .phone{font-family:"Montserrat",sans-serif;font-weight:800;}
  .on-red{fill:var(--board-white);}
  .on-white{fill:var(--brand-red);}
</style>
</head>
<body>
<svg class="canvas" viewBox="0 0 1000 360" xmlns="http://www.w3.org/2000/svg">
  <defs>
    <linearGradient id="mascot-tone" x1="0" y1="0" x2="0" y2="1">
      <stop offset="0" stop-color="#F8D3D4"/>
      <stop offset="1" stop-color="#EC4F4E"/>
    </linearGradient>
    <g id="box-net">
      <!-- board with glue flaps -->
      <path class="board" d="M35,25 H530 V36 L538,44 V218 L530,226 V232 H330 V320 H185 V345 H45 V320 H35 V230 L10,225 V122 L35,118 V112 L10,108 V32 L35,28 Z"/>
      <!-- stripes and red field -->
      <polygon class="red" points="35,25 52,25 52,232 35,232"/>
      <polygon class="red" points="180,25 195,25 287,232 272,232"/>
      <polygon class="red" points="210,25 225,25 317,232 302,232"/>
      <polygon class="red" points="240,25 255,25 347,232 332,232"/>
      <polygon class="red" points="268,25 530,25 530,232 360,232"/>

      <!-- mascot artwork areas -->
      <rect x="110" y="35" width="50" height="60" rx="14" fill="url(#mascot-tone)" role="img" aria-label="Small chicken mascot illustration"/>
      <rect x="50" y="130" width="75" height="100" rx="18" fill="url(#mascot-tone)" role="img" aria-label="Chef chicken mascot giving a thumbs up"/>

      <!-- brand name -->
      <rect class="red-soft" x="130" y="160" width="14" height="14"/>
      <text class="brand-name" x="150" y="186" font-size="36">MRW</text>

      <!-- front panel copy -->
      <text class="label on-white" x="160" y="132" font-size="7">VIEW MENU</text>
      <text class="headline" x="337" y="78" font-size="54" textLength="168" lengthAdjust="spacingAndGlyphs">CRISPY</text>
      <text class="headline" x="337" y="102" font-size="22" textLength="168" lengthAdjust="spacingAndGlyphs">CRISPY, JUICY, FINGER</text>
      <text class="headline" x="337" y="139" font-size="38" textLength="168" lengthAdjust="spacingAndGlyphs">LICKIN' GOOD!</text>

      <circle class="on-red" cx="391" cy="188.5" r="2.5"/>
      <text class="label on-red" x="396" y="191" font-size="5.5">ORDER AT CHATLINE</text>
      <text class="phone on-red" x="388" y="207" font-size="11.5">1 555 010 2737</text>
      <text class="phone on-red" x="388" y="220" font-size="11.5">1 555 010 3937</text>

      <!-- base panel copy -->
      <circle class="on-white" cx="86" cy="252.5" r="3"/>
      <text class="label on-white" x="93" y="255" font-size="6">ORDER AT CHATLINE</text>
      <text class="phone on-white" x="80" y="277" font-size="17.5">1 555 010 2737</text>
      <text class="phone on-white" x="80" y="297" font-size="17.5">1 555 010 3937</text>
    </g>
  </defs>
  <use href="#box-net" x="460"/>
  <use href="#box-net"/>
</svg>
</body>
</html>
```